Harrowgate Estates Business Card for Apartment Buildings

Create business cards for resident managers who run apartment buildings. The audience is the public who are searching for apartment rentals, and current residents who live at the apartment building. Key design element will be incorporating the company logo, however, the logo cannot dominate. The building name and manager name are more important than the logo. Current business card design leaves little room for copy, so we may need to reduce the size on the current card to allow for more space for copy.

Target Market(s)

Adults 18-65 years of age, who are looking for an apartment rental, plus current residents who live at our apartment buildings.

Industry/Entity Type

Property Management

Contact Information for Business Card

A major design element will be use of the company logo. Important property and manager contact information must be part of the design. The size of the logo will need to be reduced to make room for building and manager contact copy.

Font styles to use
Sans Serif

Colors
3176b5
000000
959595
ffffff

Requirements
Must have
• 1) Incorporate the company logo.
• 2) Use the company colors (dark blue, black/grey, over white).
• 3) FEATURE THE BUILDING NAME
• 4) FEATURE THE MANAGER NAME
• 5) The company name is less important than BUILDING and MANAGER
• 6) Manager contact information
• **SEE ATTACHED CREATIVE BRIEF**
Nice to have
• 1) Back of card logo watermark
• 2) Ability to write notes on back of carfd
Should not have
• Avoid letting the company logo dominate the card, the building name and manager are more important than the company logo.

```html
<!DOCTYPE html>
<html lang="en">
<head>
<meta charset="utf-8">
<title>Harrowgate Estates – Resident Manager Business Card</title>
<link rel="stylesheet" href="https://fonts.googleapis.com/css2?family=Source+Sans+3:wght@400;700&display=swap">
<style>
  :root {
    --stage: #e6e7e9;
    --card: #ffffff;
    --card-edge: #cfd0d2;
    --brand-blue: #0d6ca8;
    --ink: #48484a;
    --rule: #b3b3b3;
    --faint: #f1f1f2;
  }
  * { box-sizing: border-box; margin: 0; padding: 0; }
  html, body {
    width: 1200px; height: 1200px; overflow: hidden;
    background: var(--stage);
    font-family: "Source Sans 3", sans-serif;
    color: var(--ink);
  }
  .card {
    position: absolute; left: 256px; width: 688px; height: 393px;
    background: var(--card); border: 1px solid var(--card-edge); overflow: hidden;
  }
  .card--front { top: 202px; }
  .card--back { top: 645px; }

  /* Front */
  .brand-mark {
    position: absolute; left: 28px; top: 150px; width: 260px;
    display: flex; align-items: center; gap: 12px;
  }
  .brand-mark__dot { width: 34px; height: 34px; border-radius: 50%; background: var(--brand-blue); flex: none; }
  .brand-mark__name { font-size: 30px; font-weight: 700; line-height: 1.05; color: var(--ink); }

  .details { position: absolute; right: 39px; top: 38px; text-align: right; }
  .building-name { font-size: 28px; font-weight: 700; color: var(--brand-blue); line-height: 34px; letter-spacing: -0.2px; }
  .address { font-size: 20px; line-height: 26px; }
  .manager-name { font-size: 28px; font-weight: 700; color: var(--brand-blue); line-height: 34px; margin-top: 18px; letter-spacing: -0.2px; }
  .manager-role { font-size: 20px; line-height: 26px; }

  .contacts { position: absolute; right: 41px; top: 228px; list-style: none; text-align: right; }
  .contacts li { display: flex; justify-content: flex-end; align-items: center; gap: 8px; font-size: 20px; line-height: 26.3px; }
  .contacts svg { width: 18px; height: 16px; fill: var(--brand-blue); flex: none; }

  /* Back */
  .watermark {
    position: absolute; left: 180px; top: 70px; width: 380px;
    font-size: 92px; font-weight: 700; line-height: 0.95; color: var(--faint);
  }
  .back-brand {
    position: absolute; left: 0; right: 0; top: 26px;
    display: flex; justify-content: center; align-items: center; gap: 10px;
  }
  .back-brand__dot { width: 26px; height: 26px; border-radius: 50%; background: var(--brand-blue); }
  .back-brand__name { font-size: 24px; font-weight: 700; color: var(--brand-blue); }
  .back-url {
    position: absolute; left: 0; right: 0; top: 100px; text-align: center;
    font-size: 14px; letter-spacing: 1px;
  }
  .note-line { position: absolute; left: 38px; width: 621px; height: 0; border-top: 1px solid var(--rule); }
</style>
</head>
<body>

<section class="card card--front">
  <div class="brand-mark">
    <span class="brand-mark__dot"></span>
    <span class="brand-mark__name">Harrowgate Estates</span>
  </div>

  <div class="details">
    <h1 class="building-name">Linden Court Apartments</h1>
    <p class="address">2485 Marlow Avenue</p>
    <p class="address">Fairview, CA 90417</p>
    <h2 class="manager-name">Marisol Delgado</h2>
    <p class="manager-role">Resident Manager</p>
  </div>

  <ul class="contacts">
    <li>555-214-3086
      <svg viewBox="0 0 18 16" aria-label="office phone"><path d="M1 5c0-3 16-3 16 0v2h-4V5H5v2H1z"/><path d="M5 8h8l3 7H2z"/><circle cx="9" cy="11" r="1.8" fill="#fff"/></svg></li>
    <li>555-381-7642
      <svg viewBox="0 0 18 16" aria-label="mobile phone"><path d="M5 0h8v16H5zM6.3 1.5v11h5.4v-11z"/></svg></li>
    <li>555-906-1258
      <svg viewBox="0 0 18 16" aria-label="fax"><path d="M5 0h7l2 2v5H5z"/><path d="M1 7h16v9H1z"/><rect x="4" y="10" width="10" height="2" fill="#fff"/></svg></li>
    <li>marisol@harrowgateestates.com
      <svg viewBox="0 0 18 16" aria-label="email"><path d="M0 2h18v12H0z"/><path d="M1 3l8 6 8-6" fill="none" stroke="#fff" stroke-width="1.4"/></svg></li>
    <li>www.harrowgateestates.com
      <svg viewBox="0 0 18 16" aria-label="website"><circle cx="9" cy="8" r="7.5"/><g fill="none" stroke="#fff" stroke-width="1"><ellipse cx="9" cy="8" rx="3.2" ry="7.5"/><path d="M1.5 8h15M2.5 4.5h13M2.5 11.5h13M9 .5v15"/></g></svg></li>
  </ul>
</section>

<section class="card card--back">
  <div class="watermark" aria-hidden="true">Harrowgate Estates</div>
  <div class="back-brand">
    <span class="back-brand__dot"></span>
    <span class="back-brand__name">Harrowgate Estates</span>
  </div>
  <p class="back-url">www.harrowgateestates.com</p>
  <div class="note-line" style="top:171px"></div>
  <div class="note-line" style="top:230px"></div>
  <div class="note-line" style="top:290px"></div>
  <div class="note-line" style="top:348px"></div>
</section>

</body>
</html>
```